New Business Card for Innovative Tool Company

We need a new design of business card for our florida based tool manufacturing company. I will attach 2 files that we use for our logo, use whichever you feel works best for the card. Main colours are as per logo, and we can use different shades of black/white/grey for the background.

Contact Information for Business Card

Name/Jobtitle/cell
Brackwell Tools
Suite 214c
3190 Harlowmere Pkw
Orlando, FL32819
USA
name@brackwellco.example
www.brackwellco.example

Font styles to use
Sans Serif

Colors

Designer to choose colors to be used in the design.

Requirements
Must have
• Icons for Chatterly, Quiplet, Snapvista, Findora & Viewtube

```html
<!DOCTYPE html>
<html lang="en">
<head>
<meta charset="utf-8">
<title>Brackwell Tools — Business Card</title>
<link rel="stylesheet" href="https://fonts.googleapis.com/css2?family=Roboto:wght@400;500;700&display=swap">
<style>
  :root {
    --stage: #2b2b2b;
    --card-black: #050505;
    --brand-yellow: #f9ec3f;
    --ink: #111111;
    --rule: #8a8550;
    --ring-grey: #b9b9b9;
  }
  * { margin: 0; padding: 0; box-sizing: border-box; }
  html, body { width: 1200px; height: 960px; overflow: hidden; }
  body {
    background: var(--stage);
    font-family: "Roboto", Arial, sans-serif;
    position: relative;
  }
  .card {
    position: absolute;
    width: 600px;
    height: 343px;
    border-radius: 20px;
    background: var(--card-black);
    overflow: hidden;
    box-shadow: 0 6px 14px rgba(0,0,0,.55);
  }
  .card--front { left: 314px; top: 113px; }
  .card--back  { left: 311px; top: 471px; }

  .front-wave { position: absolute; inset: 0; width: 600px; height: 343px; }

  .brand-lockup {
    position: absolute;
    left: 36px;
    top: 40px;
    width: 254px;
    display: flex;
    flex-direction: column;
    align-items: center;
    gap: 8px;
  }
  .brand-ring {
    width: 72px; height: 72px;
    border: 2px solid var(--brand-yellow);
    border-radius: 50%;
  }
  .brand-name {
    color: var(--brand-yellow);
    font-weight: 700;
    font-size: 27px;
    letter-spacing: 1px;
    text-transform: uppercase;
    white-space: nowrap;
  }

  .contact-block {
    position: absolute;
    right: 31px;
    top: 168px;
    text-align: right;
    color: var(--ink);
  }
  .contact-name { font-size: 22px; font-weight: 700; line-height: 26px; }
  .contact-title { font-size: 14px; font-weight: 500; line-height: 18px; margin-bottom: 10px; }
  .contact-line {
    font-size: 14px;
    line-height: 19.5px;
    display: flex;
    justify-content: flex-end;
    align-items: center;
    gap: 6px;
  }
  .contact-line svg { width: 12px; height: 12px; flex: none; }
  .contact-address { font-size: 14px; line-height: 19px; margin-top: 9px; }

  .back-lockup {
    position: absolute;
    left: 208px;
    top: 76px;
    width: 184px;
    height: 184px;
    border: 4px solid var(--ring-grey);
    border-radius: 50%;
    display: flex;
    align-items: center;
    justify-content: center;
  }
  .back-lockup .brand-name { font-size: 22px; text-align: center; white-space: normal; line-height: 28px; }

  .social-row {
    position: absolute;
    left: 40px;
    right: 40px;
    top: 296px;
    display: flex;
    align-items: center;
    gap: 10px;
  }
  .social-rule { flex: 1; height: 1px; background: var(--rule); }
  .social-list { display: flex; gap: 10px; list-style: none; }
  .social-item {
    display: flex;
    align-items: center;
    gap: 4px;
    color: var(--brand-yellow);
    font-size: 11px;
    font-weight: 500;
  }
  .social-dot {
    width: 14px; height: 14px;
    border: 1.5px solid var(--brand-yellow);
    border-radius: 50%;
  }
</style>
</head>
<body>

<section class="card card--front">
  <svg class="front-wave" viewBox="0 0 600 343" aria-hidden="true">
    <path fill="var(--brand-yellow)" d="M0,257 C120,300 220,300 320,190 S480,50 600,56 L600,343 L0,343 Z"/>
    <path fill="var(--card-black)" d="M0,262 C130,305 240,300 335,195 S500,70 600,70 L600,77 C510,82 440,112 362,212 C262,322 120,312 0,276 Z"/>
  </svg>

  <div class="brand-lockup">
    <div class="brand-ring"></div>
    <div class="brand-name">Brackwell Tools</div>
  </div>

  <div class="contact-block">
    <div class="contact-name">DANA WHITLOCK</div>
    <div class="contact-title">CEO/FOUNDER</div>
    <div class="contact-line">689 555 0142
      <svg viewBox="0 0 12 12"><rect x="3" y="0.5" width="6" height="11" rx="1" fill="none" stroke="currentColor" stroke-width="1.3"/><rect x="5" y="9" width="2" height="1" fill="currentColor"/></svg>
    </div>
    <div class="contact-line">name@brackwellco.example
      <svg viewBox="0 0 12 12"><rect x="0.5" y="2.5" width="11" height="7" fill="currentColor"/><path d="M0.5,2.5 L6,6.5 L11.5,2.5" fill="none" stroke="#f9ec3f" stroke-width="1"/></svg>
    </div>
    <div class="contact-line">www.brackwellco.example
      <svg viewBox="0 0 12 12"><circle cx="6" cy="6" r="5.5" fill="currentColor"/><path d="M3,4 Q5,3 6,5 T9,7 M4,8 Q6,9 7,8" stroke="#f9ec3f" stroke-width="1" fill="none"/></svg>
    </div>
    <div class="contact-address">Brackwell Tools, Suite 214c<br>3190 Harlowmere Pkw, Orlando, FL32819 USA</div>
  </div>
</section>

<section class="card card--back">
  <div class="back-lockup">
    <div class="brand-name">Brackwell<br>Tools</div>
  </div>

  <div class="social-row">
    <span class="social-rule"></span>
    <ul class="social-list">
      <li class="social-item"><span class="social-dot"></span>Findora</li>
      <li class="social-item"><span class="social-dot"></span>Chatterly</li>
      <li class="social-item"><span class="social-dot"></span>Snapvista</li>
      <li class="social-item"><span class="social-dot"></span>Quiplet</li>
      <li class="social-item"><span class="social-dot"></span>Viewtube</li>
    </ul>
    <span class="social-rule"></span>
  </div>
</section>

</body>
</html>
```